Olmo Restaurant & Bar Menu

Want to make current menu more trendy in design. I have attached a pdf of the menu and of the logo. Rather, than being 6 pages I would like to make the menu into "4 pages". The menu will be printed in color.

I am open to designs that will allow the menu to be printed on 11x17 paper that will be folded in half. The "Breakfast" section needs to be its own page and all the way on the back.

As for the cover I am open to just keeping it as a cover with the info I have on it but completely different design/picture change. The logo needs to stay. The cover can also be used as having menu items on there if pulled of correctly.

The readability has to be clear to the guests.

The restaurant is a Mediterranean style and for the area it is priced mid-high. The atmosphere is casual fine dining with Martini & Wine Bar. All are ingredients are fresh never frozen and everything is prepared from scratch.

Industry/Entity Type

Restaurant

Requirements
Must have
• Breakfast on its own page on the back.
Nice to have
• Trendy Design

```html
<!DOCTYPE html>
<html lang="en">
<head>
<meta charset="utf-8">
<title>Olmo Restaurant &amp; Bar – Breakfast Menu</title>
<link rel="stylesheet" href="https://fonts.googleapis.com/css2?family=Courgette&family=Open+Sans:wght@400;600&family=Oswald:wght@400;500&family=Quicksand:wght@400&display=swap">
<style>
  :root {
    --backdrop: #45484d;
    --paper: #ffffff;
    --sky: #45ace0;
    --ink: #1d1d1d;
    --ink-soft: #555a5f;
    --charcoal: #2e2e30;
    --stripe: #0d0d0d;
  }
  * { box-sizing: border-box; margin: 0; padding: 0; }
  html, body { width: 1200px; height: 1000px; overflow: hidden; background: var(--backdrop); }
  .spread { position: absolute; left: 28px; top: 130px; width: 1144px; height: 740px; display: flex; box-shadow: 0 18px 40px rgba(0,0,0,.45); }
  .page { position: relative; width: 572px; height: 740px; background: var(--paper); overflow: hidden; }
  .photo { position: absolute; left: 0; top: 0; width: 572px; height: 740px; }

  /* Breakfast page */
  .band { position: absolute; left: 0; width: 318px; height: 30px; background: var(--sky);
          clip-path: polygon(0 0, 100% 0, 93% 100%, 0 100%);
          font-family: 'Courgette', cursive; color: #fff; font-size: 19px; line-height: 30px; padding-left: 14px; }
  .item { position: absolute; font-family: 'Oswald', sans-serif; line-height: 1.15; white-space: nowrap; }
  .item-name { color: var(--sky); font-size: 11px; text-transform: uppercase; }
  .leader { color: var(--sky); font-size: 10px; letter-spacing: 1px; margin: 0 3px; }
  .price { color: var(--ink); font-size: 12px; font-weight: 500; }
  .item-desc { font-family: 'Open Sans', sans-serif; font-size: 8.5px; line-height: 1.25; color: var(--ink-soft); margin-top: 2px; white-space: normal; }
  .page-title { position: absolute; right: 14px; top: 655px; font-family: 'Courgette', cursive; font-size: 42px;
                color: rgba(255,214,120,.9); white-space: nowrap; }

  /* Cover page */
  .brand { position: absolute; right: 26px; top: 225px; display: flex; align-items: center; gap: 10px; }
  .brand-dot { width: 28px; height: 28px; border-radius: 50%; background: var(--sky); }
  .brand-name { font-family: 'Oswald', sans-serif; font-weight: 500; font-size: 30px; color: var(--charcoal); text-transform: uppercase; letter-spacing: .5px; }
  .contact { position: absolute; left: 250px; top: 292px; width: 300px; text-align: center;
             font-family: 'Open Sans', sans-serif; font-size: 14px; line-height: 1.6; color: var(--ink); font-style: normal; }
  .contact .web { font-weight: 600; }
  .features { position: absolute; right: 26px; top: 390px; text-align: right;
              font-family: 'Courgette', cursive; font-size: 17px; line-height: 1.6; color: var(--sky); }
  .hours-band { position: absolute; left: 190px; top: 625px; width: 382px; height: 82px; background: var(--sky);
                clip-path: polygon(7% 0, 100% 0, 100% 100%, 0 100%);
                display: flex; align-items: center; gap: 14px; padding-left: 40px; }
  .hours-band svg { flex: none; }
  .hours-text { font-family: 'Quicksand', sans-serif; font-size: 24px; line-height: 1.2; color: #fff; text-align: center; }
</style>
</head>
<body>
<main class="spread">

  <!-- Back page: breakfast -->
  <section class="page breakfast-page">
    <svg class="photo" viewBox="0 0 572 740" role="img" aria-label="Photo of a grilled chicken pita with tomato and basil">
      <defs>
        <linearGradient id="pitaTones" x1="0" y1="1" x2="1" y2="0">
          <stop offset="0" stop-color="#d9c39a"/>
          <stop offset=".45" stop-color="#b5452f"/>
          <stop offset=".75" stop-color="#3f6b2e"/>
          <stop offset="1" stop-color="#2a2a22"/>
        </linearGradient>
      </defs>
      <polygon points="170,740 572,560 572,740" fill="url(#pitaTones)"/>
    </svg>

    <div class="band" style="top:16px">Skillets</div>
    <div class="item" style="left:18px;top:54px;width:185px"><span class="item-name">Veggie</span><span class="leader">......</span><span class="price">$6.95</span>
      <p class="item-desc">Skillet full of hash browns, onions, peppers, tomatoes &amp; mushrooms topped with cheese and 2 eggs. Served w/ Toast.</p></div>
    <div class="item" style="left:18px;top:104px;width:185px"><span class="item-name">Biscuits &amp; Gravy</span><span class="leader">......</span><span class="price">$7.95</span>
      <p class="item-desc">Skillet full of hash browns, onions, peppers &amp; cheese. Topped w/ homemade biscuit, sausage gravy &amp; 2 eggs.</p></div>
    <div class="item" style="left:210px;top:50px;width:165px"><span class="item-name">Irish</span><span class="leader">......</span><span class="price">$7.95</span>
      <p class="item-desc">Skillet full of hash browns, onions, peppers &amp; mushrooms topped with cheese and 2 eggs. Served w/ Toast.</p></div>
    <div class="item" style="left:384px;top:22px;width:174px"><span class="item-name">Melting Pot</span><span class="leader">......</span><span class="price">$8.95</span>
      <p class="item-desc">Skillet full of hash browns, ham, bacon, sausage, mushrooms, onions, tomatoes and peppers topped with cheese and 2 eggs. Served with toast.</p></div>

    <div class="band" style="top:160px">Omelettes</div>
    <div class="item" style="left:18px;top:196px;width:185px"><span class="item-name">Athenian</span><span class="leader">......</span><span class="price">$8.95</span>
      <p class="item-desc">Gyro off-the-cone, tomatoes, onions, olives, &amp; feta cheese. Served with side of homemade cucumber sauce.</p></div>
    <div class="item" style="left:18px;top:252px;width:185px"><span class="item-name">Deluxe</span><span class="leader">......</span><span class="price">$8.95</span>
      <p class="item-desc">Ham, bacon, sausage, mushrooms, onions, tomatoes &amp; peppers.</p></div>
    <div class="item" style="left:210px;top:196px;width:165px"><span class="item-name">Denver</span><span class="leader">......</span><span class="price">$7.95</span>
      <p class="item-desc">Ham, onion, pepper &amp; cheese</p></div>
    <div class="item" style="left:210px;top:240px;width:165px"><span class="item-name">Spinach Pesto</span><span class="leader">......</span><span class="price">$8.95</span>
      <p class="item-desc">Sun-Dried tomatoes, spinach, mushrooms &amp; cheese. Topped w/ Pesto Cream Sauce.</p></div>
    <div class="item" style="left:384px;top:198px;width:174px"><span class="item-name">Veggie</span><span class="leader">......</span><span class="price">$7.95</span>
      <p class="item-desc">Onions, peppers, tomatoes &amp; mushrooms</p></div>

    <div class="band" style="top:300px">Eggs &amp; Specialties</div>
    <div class="item" style="left:18px;top:338px"><span class="item-name">Two Eggs, Hash Browns &amp; Toast</span><span class="leader">....</span><span class="price">$4.95</span></div>
    <div class="item" style="left:18px;top:358px"><span class="item-name">Two Eggs, with Corned Beef Hash</span><span class="leader">....</span><span class="price">$6.55</span></div>
    <div class="item" style="left:18px;top:378px;width:220px"><span class="item-name">Steak &amp; Eggs</span><span class="leader">......</span><span class="price">$13.95</span>
      <p class="item-desc">8oz Prime Cut Steak, 2 Eggs, hash browns, &amp; Toast.</p></div>
    <div class="item" style="left:18px;top:410px;width:220px"><span class="item-name">3 Deuces</span><span class="leader">......</span><span class="price">$6.95</span>
      <p class="item-desc">Two Eggs, Two Pancakes &amp; Two Sausage Links or Bacon Strips.</p></div>
    <div class="item" style="left:262px;top:334px"><span class="item-name">Two Eggs, with Bacon, Sausage or Ham</span><span class="leader">....</span><span class="price">$5.95</span></div>
    <div class="item" style="left:262px;top:354px"><span class="item-name">Two Eggs, with Gyro Off-the-Cone</span><span class="leader">....</span><span class="price">$6.95</span></div>
    <div class="item" style="left:262px;top:376px;width:140px"><span class="item-name">Chop Steak &amp; Eggs</span><span class="leader">....</span><span class="price">$9.95</span>
      <p class="item-desc">10oz Chopped Sirloin Steak, 2 Eggs, hash browns, &amp; Toast</p></div>
    <div class="item" style="left:412px;top:376px;width:148px"><span class="item-name">Granny's Breakfast</span><span class="leader">....</span><span class="price">$6.95</span>
      <p class="item-desc">Two Eggs scrambled w/ potatoes, ham, onions &amp; peppers topped w/ cheese. Served with toast.</p></div>
    <div class="item" style="left:262px;top:432px"><span class="item-name">Homemade Biscuits &amp; Gravy</span><span class="leader">....</span><span class="price">Half $6.95 / Full $5.55</span></div>

    <div class="band" style="top:462px">Light Breakfast</div>
    <div class="item" style="left:18px;top:500px"><span class="item-name">Egg, Sausage, &amp; Cheese Sand</span><span class="leader">....</span><span class="price">$4.25</span></div>
    <div class="item" style="left:18px;top:520px"><span class="item-name">Bagel w/ Cream Cheese</span><span class="leader">....</span><span class="price">$2.55</span></div>
    <div class="item" style="left:18px;top:540px;width:205px"><span class="item-name">Mediterranean Pita</span><span class="leader">....</span><span class="price">$6.95</span>
      <p class="item-desc">Pesto Spread on Pita Bread w/ tomatoes, spinach, feta &amp; an Egg.</p></div>
    <div class="item" style="left:236px;top:500px"><span class="item-name">Oatmeal or Cereal $3.55 w/ Raisins</span><span class="leader">....</span><span class="price">$3.95</span></div>
    <div class="item" style="left:236px;top:520px"><span class="item-name">English Muffin or Raisin Toast</span><span class="leader">....</span><span class="price">$1.55</span></div>
    <div class="item" style="left:236px;top:540px"><span class="item-name">Fresh Fruit Bowl</span><span class="leader">....</span><span class="price">$4.95</span></div>

    <div class="band" style="top:584px">Pancakes, French Toast &amp; Waffles</div>
    <div class="item" style="left:18px;top:622px"><span class="item-name">Add Fruit Topping, Bacon, Ham or Sausage</span><span class="leader">....</span><span class="price">$1.95</span></div>
    <div class="item" style="left:18px;top:640px"><span class="item-name">Pancakes or French Toast</span><span class="leader">....</span><span class="price">(2) $4.55 / (3) $4.95</span></div>
    <div class="item" style="left:18px;top:658px"><span class="item-name">Apple Danish French Toast</span><span class="leader">....</span><span class="price">$6.95</span></div>
    <div class="item" style="left:18px;top:676px"><span class="item-name">Bananas Foster Pancakes</span><span class="leader">....</span><span class="price">$7.95</span></div>
    <div class="item" style="left:18px;top:694px"><span class="item-name">Strawberry Cake Waffle</span><span class="leader">....</span><span class="price">$7.95</span></div>
    <div class="item" style="left:18px;top:712px"><span class="item-name">Belgium Waffle</span><span class="leader">....</span><span class="price">$4.95</span></div>

    <h2 class="page-title">Breakfast</h2>
  </section>

  <!-- Front cover -->
  <section class="page cover-page">
    <svg class="photo" viewBox="0 0 572 740" role="img" aria-label="Photo of fried chicken on a golden waffle">
      <defs>
        <linearGradient id="waffleTones" x1="0" y1="0" x2=".4" y2="1">
          <stop offset="0" stop-color="#b8632a"/>
          <stop offset=".5" stop-color="#d89a4c"/>
          <stop offset="1" stop-color="#e9c98f"/>
        </linearGradient>
      </defs>
      <polygon points="0,0 282,0 12,470 0,470" fill="url(#waffleTones)"/>
    </svg>
    <svg class="photo" viewBox="0 0 572 740" aria-hidden="true">
      <polygon points="282,0 300,0 30,470 12,470" fill="var(--stripe)"/>
      <polygon points="0,470 30,470 0,520" fill="var(--stripe)"/>
    </svg>
    <svg class="photo" viewBox="0 0 572 740" role="img" aria-label="Photo of a berry dessert with whipped cream and mint">
      <defs>
        <linearGradient id="dessertTones" x1="0" y1="0" x2="1" y2="1">
          <stop offset="0" stop-color="#5f8f45"/>
          <stop offset=".3" stop-color="#f3efe6"/>
          <stop offset=".65" stop-color="#e8dccb"/>
          <stop offset=".85" stop-color="#6b1d2c"/>
          <stop offset="1" stop-color="#c9a77a"/>
        </linearGradient>
      </defs>
      <polygon points="0,470 572,590 572,740 0,740" fill="url(#dessertTones)"/>
    </svg>

    <div class="brand">
      <span class="brand-dot"></span>
      <h1 class="brand-name">Olmo Restaurant &amp; Bar</h1>
    </div>
    <address class="contact">
      <p>48 Harbor Lane · Millbrook, WI 53000</p>
      <p>555-014-2290</p>
      <p class="web">www.olmorestaurant.com</p>
    </address>
    <div class="features">
      <p>Catering &amp; Private Party Hosting Available</p>
      <p>Friday Fish Fry · Saturday Prime Rib</p>
    </div>
    <div class="hours-band">
      <svg width="30" height="30" viewBox="0 0 30 30" aria-hidden="true">
        <path d="M4 13 A11 8 0 0 1 26 13 Z" fill="#fff"/>
        <rect x="3" y="15" width="24" height="3" rx="1.5" fill="#fff"/>
        <rect x="4" y="20" width="22" height="5" rx="2" fill="#fff"/>
      </svg>
      <p class="hours-text">Serving Breakfast<br>Saturday &amp; Sunday</p>
    </div>
  </section>

</main>
</body>
</html>
```